Animal Eye Clinic needs a Business card

We are a new veterinary ophthalmology practice (Tessaly Animal Eye Care) and we need a business card designed. We only see animal eyes - we are not a regular veterinary clinic. We already have a logo. We are looking for a professional, good looking business card to hand out to our clients. We are looking for something simple but professional and contemporary. Our logo is likely the only picture/graphic that needs to be on the card.
Updates

Contact Information for Business Card

Marisol Dunkley, BSc, DVM, MSc, DipACVO
Veterinary Ophthalmologist

Phone: 250.418.3097
Email: tessalyanimaleyecare@mailbrook.net
Website: tessalyanimaleyecare.net
Address: 1840 Pellworth Rd
Kelowna, BC, V4T 8M3

Colors

Designer to choose colors to be used in the design.

Requirements
Must have
• Our logo (attached)

```html
<!DOCTYPE html>
<html lang="en">
<head>
<meta charset="utf-8">
<title>Tessaly Animal Eye Care – Business Card</title>
<link rel="stylesheet" href="https://fonts.googleapis.com/css2?family=Roboto+Condensed:wght@400;700&display=swap">
<style>
  :root {
    --backdrop: #5b5b5d;
    --card-dark: #231f20;
    --teal: #0b97a8;
    --teal-edge: #0a8797;
    --stripe-grey: #7a7a7c;
    --white: #ffffff;
    --font: "Roboto Condensed", Arial, sans-serif;
  }
  * { box-sizing: border-box; margin: 0; padding: 0; }
  html, body { width: 1200px; height: 900px; overflow: hidden; }
  body {
    background: var(--backdrop);
    font-family: var(--font);
    position: relative;
  }
  .card {
    position: absolute;
    left: 290px;
    width: 620px;
    height: 354px;
    background: var(--card-dark);
    overflow: hidden;
    box-shadow: 0 8px 24px rgba(0,0,0,.35);
  }
  .card--front { top: 72px; }
  .card--back { top: 474px; }
  .card__waves { position: absolute; inset: 0; width: 100%; height: 100%; }
  .practice-name {
    position: absolute;
    color: var(--white);
    font-weight: 400;
    white-space: nowrap;
  }
  .card--front .practice-name { left: 70px; top: 112px; font-size: 26px; }
  .card--back .practice-name { left: 40px; top: 96px; font-size: 20px; }
  .website {
    position: absolute;
    left: 48px; bottom: 40px;
    color: var(--white);
    font-size: 17px;
    font-weight: 700;
  }
  .person {
    position: absolute;
    right: 34px; top: 38px;
    text-align: right;
    color: var(--white);
  }
  .person__name {
    color: var(--teal);
    font-size: 30px;
    font-weight: 400;
    text-transform: uppercase;
    line-height: 1;
    margin-bottom: 4px;
  }
  .person__line { font-size: 13px; line-height: 1.3; }
  .contact {
    position: absolute;
    left: 34px; bottom: 22px;
    list-style: none;
    color: var(--white);
    font-size: 16px;
  }
  .contact__item { display: flex; align-items: center; gap: 10px; line-height: 1.45; }
  .contact__icon { width: 14px; height: 14px; flex: none; fill: var(--white); }
</style>
</head>
<body>

  <section class="card card--front" aria-label="Card front">
    <svg class="card__waves" viewBox="0 0 620 354" preserveAspectRatio="none" aria-hidden="true">
      <path fill="var(--stripe-grey)" d="M0,262 C170,220 300,110 620,50 L620,76 C330,130 190,240 0,276 Z"/>
      <path fill="var(--teal)" d="M0,354 L0,282 C200,260 330,150 620,86 L620,354 Z"/>
      <rect fill="var(--teal-edge)" x="0" y="348" width="620" height="6"/>
    </svg>
    <p class="practice-name">Tessaly Animal Eye Care</p>
    <p class="website">www.tessalyanimaleyecare.net</p>
  </section>

  <section class="card card--back" aria-label="Card back">
    <svg class="card__waves" viewBox="0 0 620 354" preserveAspectRatio="none" aria-hidden="true">
      <path fill="var(--stripe-grey)" d="M0,228 C170,170 330,125 620,108 L620,132 C330,150 190,200 0,240 Z"/>
      <path fill="var(--teal)" d="M0,354 L0,246 C210,205 340,160 620,140 L620,354 Z"/>
      <rect fill="var(--teal-edge)" x="0" y="348" width="620" height="6"/>
    </svg>
    <p class="practice-name">Tessaly Animal Eye Care</p>
    <div class="person">
      <h1 class="person__name">Marisol Dunkley</h1>
      <p class="person__line">BSc, DVM, MSc, DipACVO</p>
      <p class="person__line">Veterinary Ophthalmologist</p>
    </div>
    <ul class="contact">
      <li class="contact__item">
        <svg class="contact__icon" viewBox="0 0 24 24" aria-hidden="true"><path d="M6.6 10.8a15.1 15.1 0 0 0 6.6 6.6l2.2-2.2c.3-.3.7-.4 1-.2 1.1.4 2.3.6 3.6.6.6 0 1 .4 1 1V20c0 .6-.4 1-1 1A17 17 0 0 1 3 4c0-.6.4-1 1-1h3.5c.6 0 1 .4 1 1 0 1.3.2 2.5.6 3.6.1.3 0 .7-.2 1z"/></svg>
        250.418.3097
      </li>
      <li class="contact__item">
        <svg class="contact__icon" viewBox="0 0 24 24" aria-hidden="true"><path d="M12 2a7 7 0 0 0-7 7c0 5.2 7 13 7 13s7-7.8 7-13a7 7 0 0 0-7-7zm0 9.5A2.5 2.5 0 1 1 12 6.5a2.5 2.5 0 0 1 0 5z"/></svg>
        1840 Pellworth Rd, Kelowna, BC, V4T 8M3
      </li>
      <li class="contact__item">
        <svg class="contact__icon" viewBox="0 0 24 24" aria-hidden="true"><path d="M2 5h20v14H2zm2 2v.4l8 5.3 8-5.3V7zm0 2.8V17h16V9.8l-8 5.3z"/></svg>
        tessalyanimaleyecare@mailbrook.net
      </li>
    </ul>
  </section>

</body>
</html>
```